Website Landing Page for Brightfall Systems

Create a custom designed website landing page for our business. Looking for a professional upscale design that incorporates our logo and logo colors into the theme. I want a standard fixed frame website, not a constant scrolling format that seems to be the trend. To start with I'm looking for more of the graphic design part, maybe a concept or theme, I don't expect to see a finished project. Not interested in generic templates or layouts.

The name of our company is Brightfall Systems and I've attached our logo below. I'd like to have the web page have the same look and feel of our logo, as well as the colors. Our company, Brightfall Systems does system design, installation, and programming, of residential and commercial Audio/Video and Automation systems. We do home theaters, lighting and building automation, video conferencing systems, security camera installations, conference rooms, projectors, distributed audio systems, and similar Technology projects. This will be a professional services/informational website. We will not sell products on this website. This website will be used to advertise our company and communicate our services to prospective customers. Having a well designed, professional and clean website is one way we want to distinguish our company from the competition.

Here are some examples of what I consider a professional well designed website
http://www.qorlamstudio.com/Work/

Last year we had our tradlo store designed (with PixelMarket) and I'm really happy with the way it turned out. You can see it at www.HolvenGearDepot.com I consider this to be a great design and looking for the same level of quality with this new website. However, do not copy or use any part of this design in this new project. This tradlo store is completely separate from our other company Brightfall Systems. I only mention this tradlo store an an example of good work.

Reason: Still going through designs.

Reason: Still working on project and have not had time to review all designs and request revisions.

Reason: Sill going through designs and requesting revisions

Reason: still going through all the submissions we received.

Target Market(s)

People interested in Audio/Video, home theaters, home automation. We do sales, system design, and programming. We typically work on larger projects with both residential and commercial customers.

Industry/Entity Type

Business

Number of Pages Required

1 page

Requirements
Must have
• Great design elements. Please use a white background. I think white goes well with our logo colors.

```html
<!DOCTYPE html>
<html lang="en">
<head>
<meta charset="utf-8">
<title>Brightfall Systems</title>
<link rel="stylesheet" href="https://fonts.googleapis.com/css2?family=Arimo:wght@400&family=Comfortaa:wght@300&family=Montserrat:wght@800&family=Open+Sans:wght@300&family=Roboto+Condensed:wght@400;500&family=Roboto:wght@500;700&family=Noto+Serif:wght@400&display=swap">
<style>
  :root {
    --teal: #2ab3c9;
    --blue-head: #2f95c9;
    --green: #84c241;
    --green-dark: #2e5a17;
    --call-blue: #6c9bd2;
    --red: #e0382f;
    --ink: #111;
    --page: #e6ebe2;
  }
  * { margin: 0; padding: 0; box-sizing: border-box; }
  html, body { width: 866px; height: 1200px; overflow: hidden; }
  body {
    position: relative;
    background: linear-gradient(to bottom, #fff 0 68px, #c9c9c9 68px 368px, var(--page) 368px);
    font-family: "Arimo", Arial, sans-serif;
    color: var(--ink);
  }
  .header { position: absolute; left: 0; top: 0; width: 866px; height: 68px; background: #fff; }
  .brand-name { position: absolute; left: 136px; top: 22px; font-family: "Arimo", Arial, sans-serif; font-weight: 400; font-size: 21px; line-height: 24px; color: var(--teal); white-space: nowrap; }
  .search { position: absolute; left: 351px; top: 12px; width: 197px; height: 20px; background: #efefef; border: 1px solid #ddd; font-size: 7px; color: #999; padding: 6px 8px; }
  .search svg { position: absolute; right: 6px; top: 4px; }
  .call { position: absolute; left: 352px; top: 38px; font-family: "Roboto", sans-serif; font-weight: 500; font-size: 19px; color: #222; white-space: nowrap; }
  .call span { color: var(--teal); margin-right: 8px; }
  .social { position: absolute; left: 608px; top: 29px; display: flex; gap: 10px; }
  .social i { display: block; height: 10px; border-radius: 2px; }
  .hero { position: absolute; left: 0; top: 68px; width: 866px; height: 241px; background: linear-gradient(to right, #9d9d9d, #d6d6d6 12%, #d6d6d6 88%, #9d9d9d); }
  .hero-photo { position: absolute; left: 108px; top: 0; width: 650px; height: 241px; background: radial-gradient(ellipse at 50% 40%, #6a6a6a, #3d3d3d 70%, #2a2a2a); }
  .nav { position: absolute; left: 128px; top: 9px; width: 609px; height: 28px; background: #fff; font-family: "Roboto Condensed", sans-serif; font-size: 12px; color: #111; }
  .nav-home { position: absolute; left: 0; top: 0; width: 54px; height: 28px; background: var(--teal); display: flex; align-items: center; justify-content: center; }
  .nav a { position: absolute; top: 7px; color: inherit; text-decoration: none; white-space: nowrap; line-height: 14px; }
  .hero-copy { position: absolute; left: 108px; top: 69px; width: 650px; text-align: center; color: #ececec; white-space: nowrap; }
  .hero-title { font-family: "Montserrat", sans-serif; font-weight: 800; font-size: 30px; line-height: 32px; color: #e2e2e2; }
  .hero-sub { font-family: "Comfortaa", sans-serif; font-weight: 300; font-size: 19px; line-height: 20px; margin-top: 1px; }
  .hero-strong { font-family: "Montserrat", sans-serif; font-weight: 800; font-size: 22px; line-height: 24px; margin-top: 2px; }
  .cta { position: absolute; left: 316px; top: 193px; width: 244px; height: 29px; background: var(--red); color: #fff; font-family: "Roboto", sans-serif; font-weight: 700; font-size: 11px; display: flex; align-items: center; justify-content: center; white-space: nowrap; }
  .column { position: absolute; left: 108px; top: 309px; width: 650px; height: 891px; background: #fff; }
  .services { position: absolute; left: 20px; top: 13px; width: 610px; height: 489px; background: #000; }
  .services-list { color: #fff; font-family: "Roboto", sans-serif; font-weight: 500; font-size: 12.5px; line-height: 19px; text-align: center; padding-top: 6px; white-space: nowrap; }
  .gallery { position: absolute; left: 1px; top: 51px; width: 609px; height: 384px; display: grid; grid-template-columns: 303px 306px; grid-template-rows: 195px 189px; }
  .gallery div:nth-child(1) { background: linear-gradient(160deg, #b9b6b0, #6d727a 60%, #2d3744); }
  .gallery div:nth-child(2) { background: linear-gradient(170deg, #f1e2c3, #cbb595 60%, #8b7b64); }
  .gallery div:nth-child(3) { background: linear-gradient(180deg, #d9d9d9, #8c6b55 50%, #b9bcc0); }
  .gallery div:nth-child(4) { background: linear-gradient(160deg, #5c6a6b, #2f3a3a 50%, #8a5a34); }
  .arrows { position: absolute; top: 449px; left: 205px; display: flex; gap: 13px; }
  .arrows span { width: 94px; height: 28px; display: flex; align-items: center; justify-content: center; }
  .arrow-prev { background: var(--green-dark); }
  .arrow-next { background: var(--green); }
  .intro-title { position: absolute; left: 0; top: 513px; width: 650px; text-align: center; font-family: "Roboto Condensed", sans-serif; font-weight: 400; font-size: 21.5px; color: var(--blue-head); white-space: nowrap; }
  .intro { position: absolute; left: 28px; top: 548px; width: 593px; font-size: 12px; line-height: 17.5px; text-align: justify; }
  .promise { position: absolute; left: 16px; top: 621px; width: 621px; height: 73px; background: var(--green); color: #fff; font-family: "Open Sans", sans-serif; font-weight: 300; font-size: 13px; line-height: 17.5px; padding: 6px 16px; text-align: justify; }
  .tollfree { position: absolute; left: 145px; top: 714px; width: 370px; height: 66px; background: var(--call-blue); text-align: center; }
  .tollfree small { display: block; font-family: "Noto Serif", serif; font-size: 12px; margin-top: 6px; color: #111; }
  .tollfree strong { display: block; font-family: "Roboto", sans-serif; font-weight: 700; font-size: 36px; line-height: 38px; color: #fff; }
  .footer { position: absolute; left: 0; top: 808px; width: 650px; border-top: 1px solid #999; text-align: center; font-size: 12px; line-height: 20px; padding-top: 11px; color: #222; }
  .footer a { color: inherit; text-decoration: none; }
  .footer b { font-weight: 400; margin: 0 12px; }
</style>
</head>
<body>
  <header class="header">
    <div class="brand-name">Brightfall Systems</div>
    <div class="search">SEARCH
      <svg width="11" height="11" viewBox="0 0 11 11"><circle cx="4.5" cy="4.5" r="3.5" fill="none" stroke="#999" stroke-width="1.4"/><line x1="7" y1="7" x2="10" y2="10" stroke="#999" stroke-width="1.6"/></svg>
    </div>
    <div class="call"><span>CALL</span>(800) 555 0142</div>
    <div class="social"><i style="width:18px;border:1px solid #ddd;background:#fff"></i><i style="width:32px;background:#2d9de0"></i><i style="width:40px;background:#4a66a0"></i></div>
  </header>

  <section class="hero">
    <div class="hero-photo" role="img" aria-label="Dark media room with tall speakers and a low media console"></div>
    <nav class="nav">
      <span class="nav-home"><svg width="16" height="14" viewBox="0 0 16 14"><path d="M8 1 L15 7 H13 V13 H9.5 V9 H6.5 V13 H3 V7 H1 Z" fill="#fff"/></svg></span>
      <a style="left:94px">SMART HOME</a><a style="left:184px">CORPORATE</a><a style="left:265px">COMMERCIAL</a><a style="left:350px">BUILDERS</a><a style="left:426px">ABOUT</a><a style="left:481px">CONTACT</a><a style="left:549px">BLOG</a>
    </nav>
    <div class="hero-copy">
      <div class="hero-title">ENHANCE YOUR LIFESTYLE</div>
      <div class="hero-sub">and have complete control<br>with smart technology throughout</div>
      <div class="hero-strong">YOUR ENTIRE HOME</div>
    </div>
    <div class="cta">GET YOUR FREE IN-HOME ESTIMATE NOW!</div>
  </section>

  <main class="column">
    <section class="services">
      <div class="services-list">SMART HOME AUTOMATION &nbsp;|&nbsp; WHOLE HOUSE AUDIO / VIDEO &nbsp;|&nbsp; HOME LIGHTING AND SHADING<br>CUSTOM HOME-THEATER | &nbsp;OUTDOOR SYSTEM &nbsp;| &nbsp;COMMERCIAL AUTOMATION</div>
      <div class="gallery">
        <div role="img" aria-label="Auditorium with tiered seating and a projection screen"></div>
        <div role="img" aria-label="Living room with a wall-mounted television and sectional sofa"></div>
        <div role="img" aria-label="Conference room with a long table and a wall display"></div>
        <div role="img" aria-label="Restaurant bar with stools and glass walls"></div>
      </div>
      <div class="arrows">
        <span class="arrow-prev"><svg width="10" height="18" viewBox="0 0 10 18"><path d="M9 1 L1 9 L9 17" fill="none" stroke="#fff" stroke-width="1.3"/></svg></span>
        <span class="arrow-next"><svg width="10" height="18" viewBox="0 0 10 18"><path d="M1 1 L9 9 L1 17" fill="none" stroke="#fff" stroke-width="1.3"/></svg></span>
      </div>
    </section>

    <h1 class="intro-title">HOME AUTOMATION – HOME THEATER – INSTALLATION &amp; SERVICE</h1>
    <p class="intro">We design and install smart home systems that integrate the latest technology in the home automation industry. specializes in residential, commercial, corporate, educational and government Audio Visual and Automation system installations. &nbsp;From video conferencing systems, dedicated home theater systems &amp; media rooms, surveil­lance &amp; security systems, to energy, climate &amp; lighting control. Your imagination is the limit!</p>
    <p class="promise">We offer a wide range of quality products, guarantee personalized service, and possess the technical expertise to do the job right, the first time. Our highly experienced professional staff will take your project from conception to completion.</p>
    <div class="tollfree"><small>Call us Toll Free</small><strong>(800) 555 0142</strong></div>

    <footer class="footer">
      <a>Home</a><b>|</b><a>Residential Spaces</a><b>|</b><a>Commercial Spaces</a><b>|</b><a>Demo</a><b>|</b><a>Image Gallery</a><b>|</b><a>Smart Home Layout</a><b>|</b><br>
      <a>User Experience</a><b>|</b><a>Partners</a><b>|</b><a>Blog</a><b>|</b><a>Contact</a>
    </footer>
  </main>
</body>
</html>
```